Standard logo business card

We are seeking a solid, somewhat understated professional design. We are a tech company. We like fonts similar to Aptifer Slab. Front side will be white with the contact information and a small version of our primary (Light background) logo.

(We have three people so we will have three names and titles)

Back side will hold our reverse logo on dark background along with the tagline:

"Intelligent annotation solutions for complex data"

Target Market(s)

Professionals, Tech

Industry/Entity Type

Business

Contact Information for Business Card

Name
Title

Phone
Email
City, State
Website

[We will email leading designer specific contact information)

Font styles to use
Serif

Requirements
Must have
• Colors are:
• Orange RGB 245,92,23
• Blue RGB 3,34,56
Nice to have
• We like a split with the Name and Title on the right and then contact details (below) on the left.

```html
<!DOCTYPE html>
<html lang="en">
<head>
<meta charset="utf-8">
<title>Norvale – Business Card</title>
<link rel="stylesheet" href="https://fonts.googleapis.com/css2?family=Roboto+Slab:wght@400;500;700&display=swap">
<style>
  :root {
    --backdrop: #2a2a2c;
    --card-white: #ffffff;
    --brand-orange: rgb(245, 92, 23);
    --brand-navy: rgb(3, 34, 56);
    --text-dark: rgb(3, 34, 56);
    --text-light: #ffffff;
    --text-muted-light: rgba(255, 255, 255, 0.82);
    --font-main: "Roboto Slab", serif;
  }
  * { box-sizing: border-box; margin: 0; padding: 0; }
  html, body {
    width: 1200px; height: 870px; overflow: hidden;
    background: var(--backdrop);
    font-family: var(--font-main);
  }
  .canvas { position: relative; width: 1200px; height: 870px; }

  .card {
    position: absolute;
    width: 560px; height: 320px;
    overflow: hidden;
    box-shadow: 0 10px 30px rgba(0, 0, 0, 0.45);
  }

  /* Back side: reverse logo on dark ground with tagline */
  .card--back { left: 80px; top: 110px; background: var(--brand-navy); }
  .back-content {
    position: absolute; inset: 0;
    display: flex; flex-direction: column; align-items: center; justify-content: center;
    gap: 22px;
  }
  .card--back .wordmark { display: flex; align-items: center; gap: 18px; }
  .card--back .wordmark-square { width: 50px; height: 50px; background: var(--brand-orange); }
  .card--back .wordmark-name {
    font-size: 68px; font-weight: 700; color: var(--text-light);
    letter-spacing: -1px; line-height: 1;
  }
  .tagline {
    font-size: 16px; font-weight: 400; color: var(--text-muted-light);
    letter-spacing: 0.3px;
  }

  /* Front side */
  .card--front { left: 560px; top: 440px; background: var(--card-white); }
  .front-top { position: absolute; left: 0; top: 0; width: 100%; height: 150px; background: var(--card-white); }
  .front-band { position: absolute; left: 0; bottom: 0; width: 100%; height: 170px; background: var(--brand-orange); }

  .contact-list {
    position: absolute; left: 34px; top: 22px;
    list-style: none; font-size: 12.5px; color: var(--text-dark);
  }
  .contact-list li { display: flex; align-items: center; gap: 9px; height: 21px; white-space: nowrap; }
  .contact-list svg { width: 13px; height: 13px; fill: var(--text-dark); flex: none; }

  .front-logo {
    position: absolute; right: 34px; top: 58px;
    display: flex; align-items: center; gap: 10px;
  }
  .front-logo .wordmark-square { width: 26px; height: 26px; background: var(--brand-orange); }
  .front-logo .wordmark-name {
    font-size: 38px; font-weight: 700; color: var(--brand-navy);
    line-height: 1; letter-spacing: -0.5px;
  }

  .address {
    position: absolute; left: 34px; top: 26px;
    color: var(--text-light); font-size: 16px; line-height: 1.4;
  }
  .person {
    position: absolute; right: 34px; bottom: 30px; text-align: right;
    color: var(--text-light);
  }
  .person-name { font-size: 19px; font-weight: 500; letter-spacing: 1px; }
  .person-title { font-size: 14px; margin-top: 4px; }
</style>
</head>
<body>
<main class="canvas">

  <section class="card card--back" aria-label="Card back">
    <div class="back-content">
      <div class="wordmark">
        <span class="wordmark-square"></span>
        <span class="wordmark-name">Norvale</span>
      </div>
      <p class="tagline">Intelligent annotation solutions for complex data</p>
    </div>
  </section>

  <section class="card card--front" aria-label="Card front">
    <div class="front-top">
      <ul class="contact-list">
        <li><svg viewBox="0 0 16 16"><path d="M3 1h3l1 4-2 1a9 9 0 0 0 5 5l1-2 4 1v3a2 2 0 0 1-2 2A13 13 0 0 1 1 3a2 2 0 0 1 2-2z"/></svg>012 555 0147</li>
        <li><svg viewBox="0 0 16 16"><path d="M4 0h8a1 1 0 0 1 1 1v14a1 1 0 0 1-1 1H4a1 1 0 0 1-1-1V1a1 1 0 0 1 1-1zm1 2v10h6V2zm3 11a1 1 0 1 0 0 2 1 1 0 0 0 0-2z"/></svg>012 555 0148</li>
        <li><svg viewBox="0 0 16 16"><path d="M3 0h7v5H3zM1 6h14v8H1zm3 2v2h2V8zm4 0v2h2V8z"/></svg>012 555 0149</li>
        <li><svg viewBox="0 0 16 16"><path d="M1 3h14v10H1zm1 1 6 5 6-5z"/></svg>hello@norvale.com</li>
        <li><svg viewBox="0 0 16 16"><path d="M8 0a8 8 0 1 0 0 16A8 8 0 0 0 8 0zm0 1.5a6.5 6.5 0 0 1 0 13 6.5 6.5 0 0 1 0-13zM2 7.3h12v1.4H2zM7.3 2h1.4v12H7.3z"/></svg>www.norvaledata.com</li>
      </ul>
      <div class="front-logo">
        <span class="wordmark-square"></span>
        <span class="wordmark-name">Norvale</span>
      </div>
    </div>
    <div class="front-band">
      <p class="address">041,12th floor,Park<br>Harbor Road NRG</p>
      <div class="person">
        <p class="person-name">DANIEL MOREAU</p>
        <p class="person-title">Managing Director</p>
      </div>
    </div>
  </section>

</main>
</body>
</html>
```